Business card logo

Hello, I would like a business card for my law firm with a logo composed of my initials "MH". The logo is intended to appear on my business card, my letterhead, envelope and documents from my office. My first and last name (Maren Holt) and "Lawyer" must appear next to the logo. I would like the logo and the characters to be in golden color on a dark background (example black, navy blue). I would especially like a refined work on the logo which should be composed of the letters J and R.

```html
<!DOCTYPE html>
<html lang="en">
<head>
<meta charset="utf-8">
<title>Maren Holt – Lawyer – Business Card</title>
<link rel="stylesheet" href="https://fonts.googleapis.com/css2?family=Cinzel:wght@400;600;700&family=Great+Vibes&family=Lato:wght@400&display=swap">
<style>
  :root{
    --page:#e9e6e1;
    --ink:#151515;
    --ink-soft:#2a2a2a;
    --gold-light:#f1dcab;
    --gold:#d8bd84;
    --gold-deep:#b99556;
    --text-dark:#1c1c1c;
    --text-muted:#3a3a3a;
  }
  *{margin:0;padding:0;box-sizing:border-box}
  html,body{width:1200px;height:1022px;overflow:hidden;background:var(--page)}
  .card{
    position:absolute;left:100px;top:225px;width:1000px;height:571px;
    border-radius:6px;overflow:hidden;box-shadow:0 12px 30px rgba(0,0,0,.25);
  }
  .card-art{position:absolute;inset:0}
  .brand{position:absolute;left:70px;top:150px;display:flex;align-items:center;gap:18px}
  .brand-square{width:92px;height:92px;border-radius:8px;background:linear-gradient(135deg,var(--gold-light),var(--gold-deep))}
  .brand-initials{font-family:"Cinzel",serif;font-weight:600;font-size:46px;color:var(--gold);letter-spacing:4px}
  .brand-name{position:absolute;left:70px;top:270px;font-family:"Cinzel",serif;font-size:44px;letter-spacing:9px;color:var(--gold)}
  .brand-role{position:absolute;left:250px;top:318px;font-family:"Great Vibes",cursive;font-size:56px;color:var(--gold)}
  .contact{position:absolute;right:48px;top:52px;text-align:right;color:var(--text-dark);font-family:"Lato",sans-serif}
  .contact-name{font-family:"Cinzel",serif;font-weight:700;font-size:30px;letter-spacing:2px}
  .contact-role{font-size:22px;margin-bottom:26px;color:var(--text-muted)}
  .contact-line{display:flex;justify-content:flex-end;align-items:center;gap:12px;font-size:24px;line-height:1.5}
  .contact-line svg{width:20px;height:20px;flex:none}
  .address{position:absolute;left:430px;bottom:48px;font-family:"Lato",sans-serif;font-size:26px;line-height:1.3;color:var(--text-muted)}
</style>
</head>
<body>
  <div class="card">
    <svg class="card-art" viewBox="0 0 1000 571" aria-hidden="true">
      <defs>
        <linearGradient id="goldFill" x1="0" y1="0" x2="1" y2="1">
          <stop offset="0" stop-color="#c9a86a"/>
          <stop offset=".45" stop-color="#f1dcab"/>
          <stop offset="1" stop-color="#d6b57a"/>
        </linearGradient>
        <linearGradient id="inkFill" x1="0" y1="0" x2="1" y2="1">
          <stop offset="0" stop-color="#2a2a2a"/>
          <stop offset="1" stop-color="#111"/>
        </linearGradient>
      </defs>
      <rect width="1000" height="571" fill="url(#inkFill)"/>
      <path d="M640,0 C600,140 560,230 430,360 C340,450 300,510 285,571 L1000,571 L1000,0 Z" fill="url(#goldFill)"/>
      <path d="M620,70 C580,190 520,280 400,390 C320,465 290,520 280,571 L300,571 C315,520 350,470 425,400 C545,290 600,200 620,70 Z" fill="#151515"/>
      <path d="M610,20 C575,150 510,250 380,370 C330,415 300,450 290,470 C320,430 360,400 395,370 C520,260 585,160 610,20 Z" fill="url(#goldFill)"/>
    </svg>

    <div class="brand">
      <div class="brand-square"></div>
      <div class="brand-initials">MH</div>
    </div>
    <div class="brand-name">MAREN HOLT</div>
    <div class="brand-role">Lawyer</div>

    <div class="contact">
      <div class="contact-name">MAREN HOLT</div>
      <div class="contact-role">Lawyer</div>
      <div class="contact-line">555-218-4730
        <svg viewBox="0 0 20 20"><circle cx="10" cy="10" r="8.5" fill="none" stroke="#1c1c1c" stroke-width="1.6"/><path d="M7 6l2 2-1 1.5c.6 1.2 1.3 1.9 2.5 2.5L12 11l2 2-1.2 1.2C10 14 6 10 5.8 7.2Z" fill="#1c1c1c"/></svg>
      </div>
      <div class="contact-line">info@holtlegaloffice.com
        <svg viewBox="0 0 20 20"><rect x="2" y="4" width="16" height="12" fill="none" stroke="#1c1c1c" stroke-width="1.6"/><path d="M2 4l8 7 8-7" fill="none" stroke="#1c1c1c" stroke-width="1.6"/></svg>
      </div>
      <div class="contact-line">www.holtlegaloffice.com
        <svg viewBox="0 0 20 20"><circle cx="10" cy="10" r="8.5" fill="#1c1c1c"/><path d="M1.5 10h17M10 1.5c-3 3-3 14 0 17M10 1.5c3 3 3 14 0 17" fill="none" stroke="#e8d2a0" stroke-width="1.1"/></svg>
      </div>
    </div>

    <div class="address">PO Box 238, Larkvale<br>Qld 4915</div>
  </div>
</body>
</html>
```